Gate Bolts Express

THIS IS A DESIGN & BUILD COMPETITION

Im Looking for a fresh E-commerce website to sell door locks, I would like it to be more visually based, so instead of having worded categories, have then visual, with rim cylinders, euro cylinders, garage locks, oval cylinders, deadlocks, sash locks, Upvc multipoint locks, door handles, window handles, safes, padlocks etc, as picture, with a product manufacturer search feature, a video tab or banner to stream videos,
Updates

Hi Everyone,

Im looking for a fully functioning e-commerce website not a logo

Thanks
Neil

I really like this website http://steadyporch.com.au/ so make it similar to this with the blues from my logo, I will upload some random stock pictures later

Hi Everyone,

Im overwhelmed by some of the designs which have been great, however I think I need to make my vision clearer, Im looking for 12 - 16 categories - euro cylinders, rim cylinders, sashlocks, deadlocks, door handles, garage locks, safes, multipoint locks, panic hardware, padlocks, nightlatches, Post Boxes.

these are only categories, once the customer clicks on the category they will have a choice of manufacturers which will be between 4/5 Brisk, Halvern, Orbo, Fen-d-bar, Pikt, Marchwood.

The reason for this is people generally dont know what the lock on their door is called and I want a site to be visual to enable customers to source the locks they need.

This is what will make my site unique!!!!

Colour is important, I want to use the blue from my logo to keep it uniformed

I like the idea of reviewed products down the left hand side

I would like a product/ manufacturer search facility 

All the above are in your designs, but they are not all on 1 design ;0)

Thanks Everyone
Neil

Hi everyone,

Done some paint shop lol with one of the submitted designs just to show yous guys what im looking for

The12 pictures in the main part of the page are categories, not sale items

Thanks

Neil

Reason: I have extended the design period as there has been a misunderstanding with this competition, The competition is for design and build

Hi Everyone,

I have extended this competition as there was a misunderstanding with this project, It is for full design and build of an ecommerce website, not just design, I will put the prize money upto £1000 total fund, so please if you cant build your design then please withdraw them.

Thanks
Neil

Target Market(s)

The market is for DIY customers wanting to change their own locks.

Industry/Entity Type

Garage

Requirements
Must have
• It must be visually based, to help customers identify the product they need,

It must also have a banner/ picture of how to measure a euro cylinder.

I think it would work best if we have a generic category picture, then when you click the picture it then has a manufacturer page in pictures again with a brief description of what the lock offers ie, anti bump, anti snap, anti drill, British Standard etc.

must be easy to populate with stock
Nice to have
• I would like it to have geolocation for visitors ip addresses so I can see where they are staying so I can offer a fitting service.

```html
<!DOCTYPE html>
<html lang="en">
<head>
<meta charset="utf-8">
<title>Gate Bolts Express</title>
<link href="https://fonts.googleapis.com/css2?family=Questrial&family=Mulish:wght@600;700;800&display=swap" rel="stylesheet">
<style>
:root{
  --brand-blue:#0b4d97;
  --link-blue:#1b5ca6;
  --lime:#c6d400;
  --ink:#333;
  --topbar:#0d0d0d;
  --footer-grey:#e4e4e4;
  --price:#e8771f;
  --rule:#9fb6d3;
  --white:#fff;
}
*{margin:0;padding:0;box-sizing:border-box}
html,body{width:900px;height:1200px;overflow:hidden;background:var(--white)}
body{position:relative;font-family:"Questrial",sans-serif;color:var(--ink)}
a{color:inherit;text-decoration:none}
.abs{position:absolute}

.topbar{left:0;top:0;width:900px;height:21px;background:var(--topbar);color:var(--white);font:700 10px "Mulish",sans-serif}
.topbar .account{position:absolute;left:553px;top:5px}
.topbar .cart{position:absolute;left:651px;top:3px;display:flex;align-items:center;gap:5px}

.masthead{left:99px;top:21px;width:705px;height:126px;background:var(--brand-blue);color:var(--white)}
.brand{position:absolute;left:12px;top:8px;font:700 37px/34px "Questrial",sans-serif;letter-spacing:-1px;text-transform:uppercase}
.phone{position:absolute;left:518px;top:26px;display:flex;gap:10px;align-items:center}
.phone .number{font-size:20px;line-height:22px}
.phone .hours{font-size:11px}
.main-nav{position:absolute;right:25px;top:98px;display:flex;gap:30px;font:700 14px "Mulish",sans-serif}

.side-heading{width:165px;height:34px;background:var(--lime);color:var(--white);font:800 15px/34px "Mulish",sans-serif;text-align:center;text-transform:uppercase}
.category-list{left:110px;top:202px;font-size:13px;color:var(--link-blue);text-transform:uppercase;line-height:18px}
.category-list .first{text-decoration:underline}
.category-list .subs{list-style:none;color:var(--ink);text-transform:none;font-size:10px;line-height:13.5px;margin:3px 0 16px 10px}
.category-list>ul{list-style:none}

.best{left:98px;width:166px}
.best .name{font-size:12px;color:var(--link-blue);margin-left:8px}
.best .thumb{width:92px;height:56px;margin:10px 0 0 25px;border-radius:8px;background:linear-gradient(135deg,#f2f2f2,#b9b9b9)}
.best .meta{display:flex;justify-content:space-between;align-items:center;margin:6px 15px 0 5px}
.stars{color:#bbb;font-size:9px;letter-spacing:1px}
.price{color:var(--price);font-size:14px}
.best .in{font-size:9px;margin:5px 0 0 5px}
.best .in a{color:var(--link-blue);text-decoration:underline}
.sep{left:98px;top:758px;width:166px;border-top:1px dotted var(--rule)}

.hero{left:279px;top:151px;width:525px;height:231px;background:linear-gradient(100deg,#6b5545 0%,#9b8775 45%,#4e4036 100%)}
.hero h2{position:absolute;left:18px;top:140px;color:var(--white);font:800 27px "Mulish",sans-serif}
.hero .cta{position:absolute;left:20px;top:177px;width:165px;height:34px;background:var(--lime);color:var(--white);font:800 15px/34px "Mulish",sans-serif;text-align:center}

.tile{width:134px;border-left:1px dotted var(--rule);text-align:center}
.tile .pic{width:106px;height:108px;margin:12px auto 0;border-radius:6px;background:linear-gradient(140deg,#f4f4f4,#a8a8a8)}
.tile .label{font:700 11px "Mulish",sans-serif;color:var(--brand-blue);margin-top:13px;text-transform:uppercase}
.tile.end{border-right:1px dotted var(--rule)}

.footer{left:0;top:919px;width:900px;height:211px;background:var(--footer-grey)}
.fcol{position:absolute;top:30px}
.fcol h3{font:400 16px "Questrial",sans-serif;color:var(--link-blue);text-transform:uppercase;margin-bottom:6px}
.fcol li{list-style:none;font-size:11px;line-height:18px;color:var(--ink)}
.signup{display:flex;margin-top:6px}
.signup input{width:124px;height:20px;border:1px solid #9ab;font:10px "Questrial",sans-serif;padding-left:8px;color:#888}
.signup button{width:27px;height:20px;border:0;background:var(--brand-blue);display:flex;align-items:center;justify-content:center}
.fcol p{font-size:11px;line-height:18px;margin-top:12px}
.social{display:flex;gap:8px;margin-top:12px}
.social span{width:24px;height:24px;border-radius:50%;background:#a9a9a9}

.baseline{left:0;top:1130px;width:900px;height:70px;background:var(--brand-blue);color:var(--white);font:700 8.5px "Mulish",sans-serif}
.baseline .copy{position:absolute;left:110px;top:20px}
.baseline .top{position:absolute;left:757px;top:19px;font:400 9.5px "Questrial",sans-serif;text-decoration:underline}
</style>
</head>
<body>

<div class="abs topbar">
  <span class="account">Register &nbsp;|&nbsp; Log in</span>
  <span class="cart">
    <svg width="16" height="13" viewBox="0 0 16 13"><path d="M1 1h3l2 8h8l1.5-6H5" fill="none" stroke="#fff" stroke-width="1.6"/><circle cx="7" cy="11.5" r="1.2" fill="#fff"/><circle cx="13" cy="11.5" r="1.2" fill="#fff"/></svg>
    Shopping Cart ( 0 items)
  </span>
</div>

<header class="abs masthead">
  <div class="brand">Gate<br>Bolts<br>Express</div>
  <div class="phone">
    <svg width="38" height="38" viewBox="0 0 38 38"><circle cx="19" cy="19" r="17" fill="none" stroke="#fff" stroke-width="2.5"/><path d="M13 10c-2 1-3 3-2 6 2 6 6 10 12 12 3 1 5 0 6-2l-4-4-3 2c-3-1-5-4-6-6l2-3z" fill="#fff"/></svg>
    <div><div class="number">555 013 2468</div><div class="hours">Mon to Fri: 9am - 5pm</div></div>
  </div>
  <nav class="main-nav"><a>PRODUCTS</a><a>BEST SELLERS</a><a>NEW ARRIVALS</a><a>CLEARANCE</a></nav>
</header>

<div class="abs side-heading" style="left:98px;top:151px">All Categories</div>
<div class="abs category-list">
  <ul>
    <li class="first">Cylinders</li>
    <li><ul class="subs"><li>- Mortese Cylinders</li><li>- Thumbturn Cylinders</li><li>- Cylinders for Knob</li><li>- Lever Locks</li></ul></li>
    <li>Euro Cylinders</li><li>Oval Cylinders</li><li>Deadlocks</li><li>Sash Locks</li><li>Garage Locks</li><li>UPVC Multipoint Locks</li><li>Padlocks</li><li>Door Handles</li><li>Window Handles</li><li>Nightlatches</li><li>Safes</li><li>Postboxes</li><li>Panic Hardwear</li><li>Manufacturer</li>
  </ul>
</div>

<div class="abs side-heading" style="left:98px;top:577px">Best Sellers</div>
<div class="abs best" style="top:626px">
  <div class="name">Thumbturn Cylinder</div>
  <div class="thumb" role="img" aria-label="Thumbturn cylinder product photo"></div>
  <div class="meta"><span class="stars">★★★★★</span><span class="price">£ 23.45</span></div>
  <div class="in">In <a>RIM CYLINDERS</a></div>
</div>
<div class="abs sep"></div>
<div class="abs best" style="top:777px">
  <div class="name">Thumbturn Cylinder</div>
  <div class="thumb" role="img" aria-label="Thumbturn cylinder product photo"></div>
  <div class="meta"><span class="stars">★★★★★</span><span class="price">£ 23.45</span></div>
  <div class="in">In <a>RIM CYLINDERS</a></div>
</div>

<section class="abs hero" role="img" aria-label="Row of digital keypad locks on wooden locker doors">
  <h2>DIGITAL LOCKING</h2>
  <a class="cta">LEARN MORE</a>
</section>

<div class="abs tile" style="left:279px;top:414px;height:144px"><div class="pic" role="img" aria-label="Rim cylinder"></div><div class="label">Rim Cylinders</div></div>
<div class="abs tile" style="left:407px;top:414px;height:144px"><div class="pic" role="img" aria-label="Euro cylinder"></div><div class="label">Euro Cylinders</div></div>
<div class="abs tile" style="left:540px;top:414px;height:144px"><div class="pic" role="img" aria-label="Oval cylinder with keys"></div><div class="label">Oval Cylinders</div></div>
<div class="abs tile end" style="left:674px;top:414px;height:144px;width:130px"><div class="pic" role="img" aria-label="Deadlock"></div><div class="label">Deadlocks</div></div>

<div class="abs tile" style="left:279px;top:582px;height:143px"><div class="pic" role="img" aria-label="Sash lock"></div><div class="label">Sash Locks</div></div>
<div class="abs tile" style="left:407px;top:582px;height:143px"><div class="pic" role="img" aria-label="Garage lock"></div><div class="label">Garage Locks</div></div>
<div class="abs tile" style="left:540px;top:582px;height:143px"><div class="pic" role="img" aria-label="UPVC multipoint cylinder"></div><div class="label">UPVC Multipoint</div></div>
<div class="abs tile end" style="left:674px;top:582px;height:143px;width:130px"><div class="pic" role="img" aria-label="Padlock"></div><div class="label">Padlocks</div></div>

<div class="abs tile" style="left:279px;top:751px;height:144px"><div class="pic" role="img" aria-label="Door handle"></div><div class="label">Door Handles</div></div>
<div class="abs tile" style="left:407px;top:751px;height:144px"><div class="pic" role="img" aria-label="Window handle"></div><div class="label">Window Handles</div></div>
<div class="abs tile" style="left:540px;top:751px;height:144px"><div class="pic" role="img" aria-label="Nightlatch"></div><div class="label">Nightlatches</div></div>
<div class="abs tile end" style="left:674px;top:751px;height:144px;width:130px"><div class="pic" role="img" aria-label="Safe"></div><div class="label">Safes</div></div>

<footer class="abs footer">
  <div class="fcol" style="left:115px"><h3>Information</h3><ul><li>About Us</li><li>Help and FAQs</li><li>Terms and Conditions</li><li>Privacy Policy</li><li>Contact Us</li></ul></div>
  <div class="fcol" style="left:295px"><h3>All Categories</h3><ul><li>Cylinders</li><li>Locks</li><li>Accessories</li><li>Safes</li><li>Postboxes</li><li>Panic Hardwear</li><li>Manufacturer</li></ul></div>
  <div class="fcol" style="left:473px"><h3>Shopping</h3><ul><li>Help and FAQs</li><li>Payents</li><li>Shipment</li><li>Return Policy</li><li>Terms and Conditions</li><li>Privacy Policy</li><li>Contact Us</li></ul></div>
  <div class="fcol" style="left:644px;width:160px">
    <h3>Deals and Offers</h3>
    <div class="signup"><input type="text" value="Your email address..." aria-label="Email address"><button aria-label="Subscribe"><svg width="8" height="10" viewBox="0 0 8 10"><path d="M1 1l5 4-5 4" fill="none" stroke="#fff" stroke-width="1.8"/></svg></button></div>
    <p>Subscribe for our Newsletter and receive Deals and Special Offers</p>
    <div class="social"><span aria-label="Social link"></span><span aria-label="Social link"></span><span aria-label="Social link"></span><span aria-label="Email"></span><span aria-label="Social link"></span></div>
  </div>
</footer>

<div class="abs baseline">
  <span class="copy">© 2013 GATEBOLTSEXPRESS.com All Rights Reserved</span>
  <a class="top">Back to top</a>
</div>

</body>
</html>
```